Laser Tattoo Removal Business Cards

We are looking for a professional business card design for a laser tattoo removal business. Ideally looking for a black business card design. The name of the business is Lumen Ink Clearing. We place our cards at local tattoo shops so we ideally are looking for something trendy/edgy to draw both male and female clientele in.

Target Market(s)

Male/Female ages 18-60

Contact Information for Business Card

black background ideally.. hoping to stay within greys, whites and black

Font styles to use
Serif
Sans Serif

Colors
121212
a9a9a9
5c5c5c
f5f5f5
ffffff
7f7f7f
606060
848484
9d9d9d

Requirements
Must have
• Employee Info:
• Marisol Dunmore
• Chief Executive Offer
• m: 919.555.0143
• w: 919.555.0178
• f: 919.555.0192
• mdunmore@lumeninkclearing.com
• Address:
• 4185 Fenwick Pkwy, Suite 210
• Raleigh, NC 27617
• Website:
• www.lumeninkclearing.com
Nice to have
• Myabe business name on back or logo on back and employee info on the front

```html
<!DOCTYPE html>
<html lang="en">
<head>
<meta charset="utf-8">
<title>Lumen Ink Clearing — Business Cards</title>
<link rel="stylesheet" href="https://fonts.googleapis.com/css2?family=Roboto:wght@400;500&family=Roboto+Condensed:wght@500&display=swap">
<style>
  :root {
    --ink: #121212;
    --panel: #262626;
    --paper: #f5f5f5;
    --white: #ffffff;
    --mark: #2e2e2e;
    --backdrop: #5c5c5c;
  }
  * { margin: 0; padding: 0; box-sizing: border-box; }
  html, body { width: 1200px; height: 960px; overflow: hidden; }
  body {
    background: var(--backdrop);
    font-family: "Roboto", Arial, sans-serif;
    position: relative;
  }
  .card {
    position: absolute;
    width: 600px;
    height: 342px;
    overflow: hidden;
  }
  .card--front { left: 322px; top: 108px; background: var(--panel); }
  .card--back  { left: 320px; top: 494px; background: var(--ink); }

  .front-shapes { position: absolute; inset: 0; }

  .contact {
    position: absolute;
    left: 28px;
    top: 142px;
    color: var(--white);
  }
  .contact__name {
    font-family: "Roboto Condensed", Arial, sans-serif;
    font-weight: 500;
    font-size: 21px;
    letter-spacing: 0.2px;
    line-height: 24px;
  }
  .contact__title {
    font-size: 15px;
    font-weight: 500;
    line-height: 20px;
    margin-bottom: 7px;
  }
  .contact__address {
    font-size: 14px;
    line-height: 20px;
    margin-bottom: 1px;
  }
  .contact__list { list-style: none; }
  .contact__item {
    display: flex;
    align-items: center;
    font-size: 14px;
    line-height: 19.3px;
  }
  .contact__icon {
    width: 14px;
    height: 14px;
    margin-right: 9px;
    flex: none;
    fill: var(--white);
  }

  .brand {
    position: absolute;
    display: flex;
    align-items: center;
    gap: 9px;
    font-weight: 500;
    text-transform: uppercase;
    white-space: nowrap;
  }
  .brand__dot { border-radius: 50%; flex: none; }
  .brand--front {
    left: 455px; top: 78px;
    transform: translate(-50%, -50%);
    font-size: 18px; letter-spacing: 1.2px;
    color: var(--mark);
  }
  .brand--front .brand__dot { width: 10px; height: 10px; background: var(--mark); }
  .brand--back {
    left: 50%; top: 50%;
    transform: translate(-50%, -50%);
    font-size: 34px; letter-spacing: 2px;
    color: var(--white);
  }
  .brand--back .brand__dot { width: 16px; height: 16px; background: var(--white); }
</style>
</head>
<body>

<section class="card card--front" aria-label="Business card front">
  <svg class="front-shapes" width="600" height="342" viewBox="0 0 600 342" aria-hidden="true">
    <polygon points="173,0 600,0 600,342 378,342" fill="var(--paper)"/>
    <polygon points="183,0 188,0 413,342 393,342" fill="var(--panel)"/>
  </svg>

  <div class="brand brand--front">
    <span class="brand__dot"></span>
    <span class="brand__name">Lumen Ink Clearing</span>
  </div>

  <div class="contact">
    <p class="contact__name">MARISOL DUNMORE</p>
    <p class="contact__title">Chief Executive Offer</p>
    <p class="contact__address">4185 Fenwick Pkwy,<br>Suite 210, Raleigh, NC 27617</p>
    <ul class="contact__list">
      <li class="contact__item">
        <svg class="contact__icon" viewBox="0 0 24 24" aria-label="Work phone"><path d="M6.6 10.8a15 15 0 0 0 6.6 6.6l2.2-2.2c.3-.3.7-.4 1-.2 1.1.4 2.3.6 3.6.6.6 0 1 .4 1 1V20c0 .6-.4 1-1 1A17 17 0 0 1 3 4c0-.6.4-1 1-1h3.5c.6 0 1 .4 1 1 0 1.3.2 2.5.6 3.6.1.3 0 .7-.2 1z"/></svg>
        919.555.0178
      </li>
      <li class="contact__item">
        <svg class="contact__icon" viewBox="0 0 24 24" aria-label="Mobile"><path d="M7 1h10a2 2 0 0 1 2 2v18a2 2 0 0 1-2 2H7a2 2 0 0 1-2-2V3a2 2 0 0 1 2-2zm0 3v14h10V4zm5 15.5a1 1 0 1 0 0 2 1 1 0 0 0 0-2z"/></svg>
        919.555.0143
      </li>
      <li class="contact__item">
        <svg class="contact__icon" viewBox="0 0 24 24" aria-label="Fax"><path d="M7 3h10v5H7zM4 9h16a2 2 0 0 1 2 2v6h-4v4H6v-4H2v-6a2 2 0 0 1 2-2zm4 7v3h8v-3z"/></svg>
        919.555.0192
      </li>
      <li class="contact__item">
        <svg class="contact__icon" viewBox="0 0 24 24" aria-label="Email"><path d="M2 5h20v14H2zm2 2v.5l8 5 8-5V7l-8 5z"/></svg>
        mdunmore@lumeninkclearing.com
      </li>
      <li class="contact__item">
        <svg class="contact__icon" viewBox="0 0 24 24" aria-label="Website"><path d="M12 2a10 10 0 1 0 0 20 10 10 0 0 0 0-20zm-1 17.9A8 8 0 0 1 4.2 10.2L9 15v1a2 2 0 0 0 2 2zm6.9-2.5A2 2 0 0 0 16 16h-1v-3a1 1 0 0 0-1-1H8v-2h2a1 1 0 0 0 1-1V7h2a2 2 0 0 0 2-2v-.4a8 8 0 0 1 2.9 12.8z"/></svg>
        www.lumeninkclearing.com
      </li>
    </ul>
  </div>
</section>

<section class="card card--back" aria-label="Business card back">
  <div class="brand brand--back">
    <span class="brand__dot"></span>
    <span class="brand__name">Lumen Ink Clearing</span>
  </div>
</section>

</body>
</html>
```